A property investment company, looking to provide lovely sustainable homes for familys and individua

For a small investment business i am starting which will buy and refurbish unloved houses and apartments to rent out or resell. the company name is my family surname (HARGREAVE). <br/>i would like the design to be simple with maybe some emphasis on an ethical and sustainable/environmentally friendly approach with a branding of maybe trees blended with some houses and or apartments.<br/>The colours i like for this design would be mainly green on either a white or black background.
Target Market(s)
This business card is to be used for professional people such as estate agents
mortgage brokers, solicitors and trades people.
Industry/Entity Type
Real Estate
Contact Information for Business Card
owner/director-Martin hargreave
e-mail-martin@hvholdings.co.uk
website-hargreavehomeholdings.co.uk
mobile-07700945318
landline-02079460581
Look and feel

```html
<!DOCTYPE html>
<html lang="en">
<head>
<meta charset="utf-8">
<title>Hargreave — Business Card</title>
<link href="https://fonts.googleapis.com/css2?family=PT+Serif:wght@400;700&display=swap" rel="stylesheet">
<style>
  :root {
    --stage: #b9b8b8;
    --card-dark: #4e4e50;
    --card-light: #fbfbfb;
    --ink: #2b2b2b;
    --lime: #8dc63f;
    --teal: #3dbfa8;
    --white: #ffffff;
  }
  * { margin: 0; padding: 0; box-sizing: border-box; }
  html, body {
    width: 1200px; height: 880px; overflow: hidden;
    background: var(--stage);
    font-family: "PT Serif", Georgia, serif;
  }
  .canvas { position: relative; width: 1200px; height: 880px; }
  .card {
    position: absolute; width: 560px; height: 320px;
    border-radius: 22px; overflow: hidden;
  }
  .card--front { left: 60px; top: 80px; background: var(--card-dark); }
  .card--back  { left: 580px; top: 480px; background: var(--card-light); }

  .brand {
    position: absolute; display: flex; align-items: center; gap: 14px;
    color: var(--lime); font-weight: 700;
  }
  .brand__dot { border-radius: 50%; background: var(--teal); flex: none; }
  .card--front .brand { left: 50%; top: 50%; transform: translate(-50%, -50%); font-size: 58px; }
  .card--front .brand__dot { width: 30px; height: 30px; }
  .card--back .brand { right: 38px; top: 44px; font-size: 38px; gap: 10px; }
  .card--back .brand__dot { width: 20px; height: 20px; }

  .accent-tab {
    position: absolute; left: -10px; top: 170px; width: 38px; height: 54px;
    background: var(--teal); border-radius: 10px;
  }
  .holder { position: absolute; left: 44px; top: 162px; color: var(--ink); font-weight: 700; }
  .holder__name { font-size: 26px; line-height: 1.15; }
  .holder__role { font-size: 22px; line-height: 1.2; }

  .contacts { position: absolute; left: 66px; top: 232px; list-style: none; }
  .contacts li {
    display: flex; align-items: center; gap: 8px;
    font-size: 16px; line-height: 1; height: 20px; margin-bottom: 2px; color: var(--ink);
  }
  .contacts svg { width: 18px; height: 18px; flex: none; }
</style>
</head>
<body>
<main class="canvas">
  <section class="card card--front" aria-label="Card front">
    <div class="brand"><span class="brand__dot"></span><span class="brand__name">Hargreave</span></div>
  </section>

  <section class="card card--back" aria-label="Card back">
    <div class="brand"><span class="brand__dot"></span><span class="brand__name">Hargreave</span></div>
    <div class="accent-tab"></div>
    <div class="holder">
      <p class="holder__name">Martin hargreave</p>
      <p class="holder__role">Director</p>
    </div>
    <ul class="contacts">
      <li>
        <svg viewBox="0 0 18 18" aria-hidden="true"><circle cx="9" cy="9" r="9" fill="#8dc63f"/><rect x="6" y="3.5" width="6" height="11" rx="1.2" fill="none" stroke="#fff" stroke-width="1.3"/><circle cx="9" cy="12.3" r=".8" fill="#fff"/></svg>
        07700945318
      </li>
      <li>
        <svg viewBox="0 0 18 18" aria-hidden="true"><circle cx="9" cy="9" r="9" fill="#8dc63f"/><path d="M4 7.5c0-2 10-2 10 0v1h-2.5V7.3h-5v1.2H4z" fill="#fff"/><rect x="5.5" y="9" width="7" height="4.5" rx="1" fill="#fff"/></svg>
        02079460581
      </li>
      <li>
        <svg viewBox="0 0 18 18" aria-hidden="true"><circle cx="9" cy="9" r="9" fill="#8dc63f"/><rect x="4" y="5.5" width="10" height="7" fill="#fff"/><path d="M4 5.5l5 4 5-4" fill="none" stroke="#8dc63f" stroke-width="1"/></svg>
        martin@hvholdings.co.uk
      </li>
      <li>
        <svg viewBox="0 0 18 18" aria-hidden="true"><circle cx="9" cy="9" r="9" fill="#8dc63f"/><g fill="none" stroke="#fff" stroke-width="1"><circle cx="9" cy="9" r="5.5"/><ellipse cx="9" cy="9" rx="2.4" ry="5.5"/><path d="M3.5 9h11M4.5 6h9M4.5 12h9"/></g></svg>
        hargreavehomeholdings.co.uk
      </li>
    </ul>
  </section>
</main>
</body>
</html>
```